Website for Kitchen Showroom

We need a website for our Kitchen Showroom. Will be 10 pages in total. Example of a website we like can be found at http://www.brivantaform.co.uk/ with the image on the front page being a java script slideshow picking up images from a directory that I can update. Looking for simple SEO
I have the wording/ sitemap/ images all ready to go and I am looking for a quick turn around.
Thank you for your time. Tom

```html
<!DOCTYPE html>
<html lang="en">
<head>
<meta charset="utf-8">
<title>Hearthline Kitchens – Kitchen Showroom</title>
<link href="https://fonts.googleapis.com/css2?family=Arimo:wght@400;700&display=swap" rel="stylesheet">
<style>
  :root {
    --green: #3f9a12;
    --green-light: #6cc42a;
    --green-dark: #2f7a0a;
    --green-text: #3a8a0c;
    --grey-logo: #8a8a8a;
    --ink: #3a3a3a;
    --nav-active: #3c3c3c;
    --bg-top: #6a6a6a;
    --bg-bottom: #575757;
    --white: #ffffff;
  }
  * { margin: 0; padding: 0; box-sizing: border-box; }
  html, body { width: 1200px; height: 1163px; overflow: hidden; }
  body {
    font-family: "Arimo", Arial, sans-serif;
    background: linear-gradient(var(--bg-top) 0, var(--bg-top) 706px, var(--bg-bottom) 706px);
    position: relative;
  }
  .site-header { position: absolute; inset: 0 0 auto 0; height: 160px; background: var(--white); }
  .brand { position: absolute; left: 26px; top: 28px; display: flex; align-items: center; gap: 22px; }
  .brand-square { width: 96px; height: 96px; background: var(--green-light); }
  .brand-name { font-size: 52px; line-height: 50px; color: var(--grey-logo); font-weight: 400; }
  .social { position: absolute; left: 1026px; top: 68px; width: 152px; height: 31px; border: 1px solid #d8d8d8;
    display: flex; align-items: center; justify-content: center; gap: 7px; }
  .social-item { width: 22px; height: 22px; background: var(--green); }
  .call { position: absolute; right: 22px; top: 116px; font-size: 29px; color: var(--ink); }
  .call-label { color: var(--green-text); font-weight: 700; }
  .main-nav { position: absolute; left: 0; top: 160px; width: 1200px; height: 57px;
    background: linear-gradient(#6cc42a, #4aa315 55%, #3f8f10); border-bottom: 1px solid #2f6e09; }
  .nav-link { position: absolute; top: 0; height: 57px; line-height: 57px; color: var(--white);
    font-weight: 700; font-size: 19px; text-decoration: none; }
  .nav-link.is-active { top: -3px; height: 60px; line-height: 62px; background: var(--nav-active);
    left: 24px; width: 97px; text-align: center; }
  .search { position: absolute; left: 909px; top: 17px; width: 228px; height: 27px; background: var(--white);
    border: 1px solid #9bd16b; font: 12px "Arimo", sans-serif; color: #555; padding: 6px 8px; }
  .search-btn { position: absolute; left: 1139px; top: 17px; width: 39px; height: 27px; background: var(--green-dark);
    border: 1px solid #9bd16b; color: var(--white); font-weight: 700; font-size: 14px; text-align: center; line-height: 25px; }
  .hero { position: absolute; left: 24px; top: 244px; width: 1152px; height: 544px; background: var(--white); }
  .hero-photo { position: absolute; left: 14px; top: 15px; width: 1124px; height: 445px;
    background: linear-gradient(100deg, #7a4a26 0%, #b57a45 35%, #d8c3a3 60%, #9ab07a 80%, #8a5630 100%); }
  .hero-title { position: absolute; left: 17px; top: 478px; font-size: 20px; font-weight: 700; color: var(--green-text); }
  .hero-text { position: absolute; left: 17px; top: 504px; font-size: 16px; color: var(--ink); }
  .hero-base { position: absolute; left: 24px; top: 788px; }
  .about-title { position: absolute; left: 26px; top: 852px; font-size: 36px; font-weight: 700; color: var(--white); }
  .about-photo { position: absolute; left: 26px; top: 920px; width: 186px; height: 132px; border: 3px solid var(--white);
    background: linear-gradient(135deg, #c9a87a, #8a6a45 60%, #5a4a3a); }
  .about-text { position: absolute; left: 238px; top: 917px; width: 942px; color: var(--white); font-size: 13px; line-height: 18px; }
  .about-text p { margin-bottom: 18px; }
  .about-text a { color: #b8ef7a; }
  .site-footer { position: absolute; left: 0; top: 1121px; width: 1200px; height: 42px;
    background: linear-gradient(#5fb823, #3f9a12); color: var(--white); font-size: 13px; line-height: 42px; }
  .footer-nav { position: absolute; left: 24px; }
  .footer-legal { position: absolute; right: 26px; }
</style>
</head>
<body>
  <header class="site-header">
    <div class="brand">
      <span class="brand-square"></span>
      <span class="brand-name">hearthline<br>kitchens</span>
    </div>
    <div class="social" aria-label="Social links">
      <span class="social-item"></span><span class="social-item"></span><span class="social-item"></span><span class="social-item"></span><span class="social-item"></span>
    </div>
    <p class="call"><span class="call-label">Call us:</span> 1800-000-000</p>
  </header>

  <nav class="main-nav">
    <a class="nav-link is-active" href="#">HOME</a>
    <a class="nav-link" style="left:153px" href="#">DESIGN</a>
    <a class="nav-link" style="left:277px" href="#">GALLERY</a>
    <a class="nav-link" style="left:414px" href="#">QUALITY</a>
    <a class="nav-link" style="left:547px" href="#">CONTACT US</a>
    <a class="nav-link" style="left:719px" href="#">LINKS</a>
    <div class="search">Search</div>
    <div class="search-btn">OK</div>
  </nav>

  <section class="hero">
    <div class="hero-photo" role="img" aria-label="Showroom kitchen with timber cabinets, stone island and a bright window"></div>
    <h2 class="hero-title">Lorem ipsum dolor sit amet, consectetur adipiscing elit.</h2>
    <p class="hero-text">Phasellus et neque a lectus vehicula rhoncus. Maecenas mauris metus, facilisis non pharetra vel, fringilla lobortis ipsum.</p>
  </section>
  <svg class="hero-base" width="1152" height="44" viewBox="0 0 1152 44" aria-hidden="true">
    <defs>
      <linearGradient id="baseGreen" x1="0" y1="0" x2="0" y2="1">
        <stop offset="0" stop-color="#3f9a12"/><stop offset="0.5" stop-color="#72c92e"/><stop offset="1" stop-color="#4aa315"/>
      </linearGradient>
    </defs>
    <polygon points="14,0 1138,0 1112,42 40,42" fill="#ffffff"/>
    <polygon points="26,0 1126,0 1104,32 48,32" fill="url(#baseGreen)"/>
  </svg>

  <main>
    <h1 class="about-title">About Hearthline Kitchens</h1>
    <div class="about-photo" role="img" aria-label="Timber kitchen interior with island bench"></div>
    <div class="about-text">
      <p>Welcome to Hearthline Kitchens. WA's exclusive kitchen manufacturer based in Westmere Perth. If you are seeking the highest quality kitchen, yet at a price that is a little more affordable, Hearthline Kitchens is the company you've been searching for.</p>
      <p>Hearthline Kitchens showroom is located less than 25 kilometers from Perth CBD, so easy to get to with easy access from the Coastal Highway.</p>
      <p>On this site, you can view some of our designer kitchens, read testimonials from our clients or just browse through our site to find out more. We hope you will find our site inspiring and put Hearthline Kitchens at the top of your list of kitchen showrooms you simply must visit.</p>
      <p>Pop into our showroom. We can chat about your plans and ideas for your new kitchen and maybe we can give you a few ideas of our own. Or <a href="#">contact us</a> to arrange a no obligation consultation with one of our kitchen designers and if required we will bring the showroom to you.</p>
    </div>
  </main>

  <footer class="site-footer">
    <span class="footer-nav">Home &nbsp;|&nbsp; Design &nbsp;|&nbsp; Gallery &nbsp;|&nbsp; Quality &nbsp;|&nbsp; Contact Us &nbsp;|&nbsp; Links</span>
    <span class="footer-legal">© 2011 hearthline kitchens . All rights reserved. &nbsp;Terms of use . Privacy Policy</span>
  </footer>
</body>
</html>
```